Corvendal needs a Pet supplement label design

We are Corvendal, a private label company located in California. We private label all natural pet products, mainly supplements and vitamins for dogs and cats of all sizes and breeds. This product is Wild Alaskan Salmon Oil for dogs and cats of all sizes and breeds. The product is a 16 oz bottle of Wild Alaskan Salmon Oil rich in EPA and DHA Omega 3s for dogs and cats (please see picture attached for a picture of what the bottle looks like).
The primary design will be the 16 oz bottle size
The secondary design will be the 32 oz bottle size (only winner will do the 32 oz design).
Size dimensions:
16oz - 8.25 x 4.00 inches (209.55 x 101.6 millimeters)
32oz - 9.8425 x 5.512 inches (250 x 140 millimeters) (only winner will do the 32 oz design)
Information on label:
Center of label:
-please use corvendal logo some place on the front of the label.
- you may add a dog and cat picture on the label design
- you may add dog and cat paw prints on the label design
-you may add picture of a salmon somewhere in the lettering/background or on the bottle
-please choose colors that will go along with the colors of the corvendal logo as well as matching a concept that relates to Salmon Oil.
Name of Brand: Corvendal (see logo attached)
Title of Product: Wild Alaskan Salmon Oil
Rich in EPA and DHA Omega 3 and Omega 6 Fatty Acids.

For Dogs and Cats

Supports and promotes heart health, healthy Skin, glossier coat, joints, healthy immune system, and brain development
All-natural with no preservatives.

Side 1: Left side, About: Corvendal's Wild Caught Alaskan Salmon Oil is made from the body oils of wild caught salmon from the Pacific Ocean in Alaska. Pharmaceutical and human grade in accordance with pharmacopeia. These fish oils are molecularly distilled to remove contaminants such as PCBs, mercury, toxins and metals. Each batch is tested by a third party lab verifying each batch exceeds the stringent quality standards set by California’s proposition 65.

Caution: Not intended for human consumption. Product is for pet consumption only. When unsealed store at room temperature away from light. Refrigerate after opening. Not to be used as a meal replacement.

These statements have not been evaluated by the food and drug administration. This product is not intended to treat, cure or prevent any disease

Still side 1: left side:
Suggested use chart: (compare to other product's charts as displayed in the photos attached. serving size amounts per weight are the same).
Add on top of your pets food and mix
body weight: pump strokes:
up to 12 lbs 1/2
12-25 lbs 1
25-50 lbs 2
50-75 lbs 3
over 75 lbs 4

Side 2: Right side
Nutritional Info Chart: per serving (5ml or 1 tsp)
Total fat (g) (TBA)
Saturated (g) (TBA)
Monounsaturated (g) (TBA)
Polyunsaturated (g) (TBA)
*Total omega 3 (mg) 1,227
*EPA (mg) 423
*DHA (mg) 465
*Not recognized as an essential nutrient by the AAFCO.

Dog Food nutrient profile

Guaranteed analysis chart:
per serving (5ml or 1 tsp)
Crude Fat 99.9 % (min)
Moisture .1 % (max)
*Omega 3 Fatty acids 30% (min)
*DHA 11% (min)
*EPA 10% (min)
*Other Omega 3 5.0 % (min)
*Omega-6 Fatty Acids 4.0 % (min)
* Not recognized as an essential nutrient by the AAFCO.

Dog Food nutrient profile

Ingredients: Wild Caught Alaskan Salmon Oil, all-natural non GMO Vitamin E

Made in USA logo, All natural ingredients logo
( I have attached all natural and human grade logos below). Please use if you can find image on account such as pixelbarn or photovaultix.

Add sku number: K774QB2R5T Create barcode for sku number (may be done after winner is selected)

Add anywhere on bottle:
Health benefits of Omega 3 fish oil for pets:
supports cardiovascular health, joints, brain development, immune system, eyes, healthy skin and shin coat, relief from dry itchy skin, overall health and vitality.

Distributed by:
CORVENDAL
872 N. BRISKET HILL RD. #214-958
SAN MARCOS, CA 92143
www.corvendalpetcare.example

* I attached several examples in the photos below of other wild salmon oil to give you an idea of what other projects look like.
Updates

Target Market(s)

Cats and Dogs of all ages, sizes and breeds.

Industry/Entity Type

It Company

Colors

Designer to choose colors to be used in the design.

Requirements
Must have
• All or majority of the included items listed in the project description
Nice to have
• Please blend the design of the label to where it will match the colors of the corvendal logo. Add any additional colors you think will go well.

```html
<!DOCTYPE html>
<html lang="en">
<head>
<meta charset="utf-8">
<title>Corvendal Wild Alaskan Salmon Oil – Front Label</title>
<link rel="stylesheet" href="https://fonts.googleapis.com/css2?family=Lilita+One&family=Quicksand:wght@600&family=Cabin:wght@500;600&family=Oswald:wght@500&display=swap">
<style>
  :root{
    --stage:#3c3c3c;
    --label-light:#f1f3f2;
    --label-mid:#dfe3e1;
    --green:#2f8a2b;
    --green-dark:#1f6a1d;
    --green-bright:#4aa83a;
    --navy:#0d3f8f;
    --gold:#f2d21d;
    --white:#ffffff;
    --ink:#2b2b2b;
    --dog-tone:#e7d3a4;
    --cat-tone:#f3c22a;
    --salmon-tone:#2f6fb7;
    --emblem-tone:#cbb991;
  }
  *{box-sizing:border-box;margin:0;padding:0}
  html,body{width:1200px;height:1200px;overflow:hidden;background:var(--stage)}
  .label{
    position:absolute;left:281px;top:95px;width:637px;height:1010px;
    background:radial-gradient(ellipse at 50% 45%,var(--label-light) 0%,var(--label-mid) 100%);
    overflow:hidden;
  }
  .top-band{
    position:absolute;left:0;top:0;width:100%;height:52px;
    background:linear-gradient(180deg,var(--green-bright),var(--green));
    display:flex;align-items:center;justify-content:center;
    font-family:"Quicksand",sans-serif;font-weight:600;font-size:24px;
    letter-spacing:5px;color:var(--white);
  }
  .top-rule{position:absolute;left:0;top:68px;width:100%;height:9px;background:var(--green)}
  .title{
    position:absolute;left:0;width:100%;text-align:center;
    font-family:"Lilita One",sans-serif;line-height:1;color:var(--green);
  }
  .title-line1{top:160px;font-size:68px;letter-spacing:1px}
  .title-line1 .alaskan{color:var(--navy)}
  .title-line2{top:252px;font-size:80px;letter-spacing:1px}
  .salmon-o{
    display:inline-block;width:60px;height:62px;vertical-align:-4px;
    border-radius:50%;
    background:radial-gradient(circle at 45% 40%,#8fb4de 0%,var(--salmon-tone) 75%);
  }
  .art{position:absolute}
  .art-dog{left:0;top:430px;width:208px;height:318px;
    background:linear-gradient(160deg,var(--dog-tone),#c9a46a);border-radius:40% 40% 10% 10%}
  .art-cat{left:456px;top:482px;width:181px;height:266px;
    background:linear-gradient(160deg,var(--cat-tone),#e59a17);border-radius:40% 40% 10% 10%}
  .hill{position:absolute;left:0;top:680px;width:637px;height:330px}
  .emblem{
    position:absolute;left:143px;top:403px;width:338px;height:338px;border-radius:50%;
    border:16px solid var(--green-dark);background:var(--white);
    display:flex;flex-direction:column;align-items:center;justify-content:center;
  }
  .emblem-art{width:220px;height:170px;border-radius:50% 50% 12px 12px;
    background:radial-gradient(circle at 50% 40%,#fff6cf 0%,var(--emblem-tone) 70%)}
  .brand-name{
    margin-top:14px;font-family:"Cabin",sans-serif;font-weight:600;
    font-size:30px;letter-spacing:3px;color:var(--green-dark);
  }
  .benefits{position:absolute;left:0;top:775px;width:100%}
  .benefits h2{
    text-align:center;font-family:"Cabin",sans-serif;font-weight:600;
    font-size:31px;color:var(--gold);letter-spacing:-.3px;
  }
  .benefit-list{
    list-style:none;display:grid;grid-template-columns:162px 250px;
    column-gap:8px;row-gap:4px;margin:8px 0 0 124px;
    font-family:"Cabin",sans-serif;font-weight:500;font-size:17px;color:var(--white);
  }
  .benefit-list li{display:flex;align-items:center;gap:8px;height:23px;white-space:nowrap}
  .benefit-list svg{width:14px;height:14px;flex:none}
  .omega-band{
    position:absolute;left:0;top:946px;width:100%;height:42px;background:var(--white);
    border-top:6px solid var(--green);
    display:flex;align-items:center;justify-content:center;
    font-family:"Oswald",sans-serif;font-weight:500;font-size:19px;letter-spacing:3px;
    color:var(--ink);white-space:nowrap;
  }
  .omega-band .acid{color:var(--green)}
  .bottom-rule{position:absolute;left:0;top:988px;width:100%;height:10px;background:var(--green)}
</style>
</head>
<body>
<main class="label">
  <div class="top-band">FOR DOGS AND CATS</div>
  <div class="top-rule"></div>

  <h1 class="title title-line1">WILD <span class="alaskan">ALASKAN</span></h1>
  <div class="title title-line2">SALM<span class="salmon-o" role="img" aria-label="Salmon leaping through the letter O"></span>N OIL</div>

  <svg class="hill" viewBox="0 0 637 330" aria-hidden="true">
    <path d="M0 62 Q318 -20 637 62 V330 H0 Z" fill="var(--green)"/>
  </svg>

  <div class="art art-dog" role="img" aria-label="Cartoon dog sitting and smiling"></div>
  <div class="art art-cat" role="img" aria-label="Cartoon orange tabby cat sitting and smiling"></div>

  <div class="emblem">
    <div class="emblem-art" role="img" aria-label="Dog and cat silhouettes before a sunburst"></div>
    <div class="brand-name">CORVENDAL</div>
  </div>

  <section class="benefits">
    <h2>SUPPORTS AND PROMOTES</h2>
    <ul class="benefit-list">
      <li><svg viewBox="0 0 14 14"><path d="M1 7.5l4 4L13 2" fill="none" stroke="#fff" stroke-width="2.4"/></svg>HEART HEALTH</li>
      <li><svg viewBox="0 0 14 14"><path d="M1 7.5l4 4L13 2" fill="none" stroke="#fff" stroke-width="2.4"/></svg>HEALTHY IMMUNE SYSTEM</li>
      <li><svg viewBox="0 0 14 14"><path d="M1 7.5l4 4L13 2" fill="none" stroke="#fff" stroke-width="2.4"/></svg>HEALTHY SKIN</li>
      <li><svg viewBox="0 0 14 14"><path d="M1 7.5l4 4L13 2" fill="none" stroke="#fff" stroke-width="2.4"/></svg>BRAIN DEVELOPMENT</li>
      <li><svg viewBox="0 0 14 14"><path d="M1 7.5l4 4L13 2" fill="none" stroke="#fff" stroke-width="2.4"/></svg>GLOSSIER COAT</li>
      <li><svg viewBox="0 0 14 14"><path d="M1 7.5l4 4L13 2" fill="none" stroke="#fff" stroke-width="2.4"/></svg>ALL-NATURAL</li>
      <li><svg viewBox="0 0 14 14"><path d="M1 7.5l4 4L13 2" fill="none" stroke="#fff" stroke-width="2.4"/></svg>JOINTS</li>
      <li><svg viewBox="0 0 14 14"><path d="M1 7.5l4 4L13 2" fill="none" stroke="#fff" stroke-width="2.4"/></svg>NO PRESERVATIVES</li>
    </ul>
  </section>

  <div class="omega-band">RICH IN&nbsp;<span class="acid">EPA</span>&nbsp;AND&nbsp;<span class="acid">DHA</span>&nbsp;OMEGA 3 AND OMEGA 6 FATTY ACIDS</div>
  <div class="bottom-rule"></div>
</main>
</body>
</html>
```